The Brambury Firm

We need a new design for our letterhead and envelopes. We are a personal injury and criminal defense firm so we need something modern and clean, but more on the professional/traditional side. Our new logo has two colors and is attached to the file so we need something that works well with those colors/matches the design. The following information needs to be on the letterhead:
Phone: (555) 314-7265
Fax: (555) 419-6032
Toll-Free: (555) 736-1149
Post Office Box 4273
Lexington, SC 29458-4273
TQHarmClaimsDesk.example
PalmettoShieldCounsel.example

Target Market(s)

Clients, government agencies, other law firms

Industry/Entity Type

Legal

Font styles to use
Sans Serif
Other font styles liked:
• Arial

Colors

Designer to choose colors to be used in the design.

Requirements
Must have
• Must look professional and clean, modern
Nice to have
• I would like to see a design that works with the logo but does not distract from the content that will be printed on it
Should not have
• Too many colors or crazy designs.

```html
<!DOCTYPE html>
<html lang="en">
<head>
<meta charset="utf-8">
<title>The Brambury Firm — Stationery</title>
<link rel="stylesheet" href="https://fonts.googleapis.com/css2?family=Open+Sans:wght@400;600&display=swap">
<style>
  :root {
    --backdrop: #d9d9d9;
    --paper: #efefef;
    --navy: #2e2d8c;
    --flap: #4645a0;
    --accent-red: #d11f26;
    --ink: #555555;
    --ink-dark: #3a3a3a;
    --band-text: #ffffff;
  }
  * { box-sizing: border-box; margin: 0; padding: 0; }
  html, body { width: 1200px; height: 810px; overflow: hidden; }
  body {
    background: var(--backdrop);
    font-family: "Open Sans", Arial, sans-serif;
    color: var(--ink);
    position: relative;
  }
  .sheet {
    position: absolute;
    background: var(--paper);
  }
  .brand {
    position: absolute;
    display: flex;
    align-items: center;
    gap: 7px;
  }
  .brand-dot {
    width: 16px; height: 16px;
    border-radius: 50%;
    background: var(--accent-red);
    flex: none;
  }
  .brand-name {
    color: var(--navy);
    font-weight: 600;
    font-size: 17px;
    letter-spacing: 0.3px;
    white-space: nowrap;
  }
  .web-band {
    position: absolute;
    left: 0; right: 0;
    height: 20px;
    background: var(--navy);
    color: var(--band-text);
    font-size: 7.4px;
    display: flex;
    align-items: center;
    justify-content: center;
    gap: 6px;
  }

  /* Letterhead */
  .letterhead { left: 137px; top: 110px; width: 436px; height: 614px; }
  .letterhead .brand { left: 38px; top: 58px; }
  .contact-block {
    position: absolute;
    left: 308px; top: 54px;
    font-size: 7.4px;
    line-height: 9.2px;
    color: var(--ink-dark);
  }
  .contact-block .address { margin-bottom: 6px; }
  .contact-row { display: flex; }
  .contact-row .label { color: var(--navy); width: 32px; }
  .recipient {
    position: absolute;
    left: 38px; top: 201px;
    font-size: 7.6px;
    line-height: 11.4px;
  }
  .body-text {
    position: absolute;
    left: 38px;
    width: 362px;
    font-size: 7.2px;
    line-height: 11.4px;
    text-align: justify;
  }
  .body-text.first { top: 268px; }
  .body-text.second { top: 370px; }
  .signature {
    position: absolute;
    left: 38px; top: 436px;
    width: 82px; height: 54px;
    background: linear-gradient(135deg, rgba(46,45,140,0.18), rgba(46,45,140,0.06));
  }
  .sign-title {
    position: absolute;
    left: 37px; top: 501px;
    font-size: 7.4px;
  }
  .letterhead .web-band { top: 576px; }

  /* Envelope back */
  .envelope-back { left: 619px; top: 194px; width: 444px; height: 221px; }
  .envelope-back .flap { position: absolute; left: 0; top: 0; }
  .flap-mark {
    position: absolute;
    left: 216px; top: 24px;
    width: 12px; height: 12px;
    border-radius: 50%;
    background: var(--paper);
  }

  /* Envelope front */
  .envelope-front { left: 618px; top: 444px; width: 445px; height: 221px; }
  .envelope-front .brand { left: 19px; top: 48px; }
  .return-address {
    position: absolute;
    left: 19px; top: 93px;
    font-size: 7.2px;
    line-height: 9.2px;
    color: var(--ink-dark);
  }
  .envelope-front .web-band { top: 185px; }
</style>
</head>
<body>

<section class="sheet letterhead">
  <div class="brand">
    <span class="brand-dot"></span>
    <span class="brand-name">The Brambury Firm</span>
  </div>

  <div class="contact-block">
    <p class="address">Post Office Box 4273<br>Lexington, SC 29458-4273</p>
    <p class="contact-row"><span class="label">Phone</span>:&nbsp;(555) 314-7265</p>
    <p class="contact-row"><span class="label">Fax</span>:&nbsp;(555) 419-6032</p>
    <p class="contact-row"><span class="label">Toll-Free</span>:&nbsp;(555) 736-1149</p>
  </div>

  <p class="recipient">Dear Harwell<br>Quillmore Print Works<br>Department Design</p>

  <p class="body-text first">Lorem ipsum dolor sit amet, consectetuer adipiscing elit. Aenean commodo ligula eget dolor. Aenean massa. Cum sociis natoque penatibus et magnis dis parturient montes, nascetur ridiculus mus. Donec quam felis, ultricies nec, pellentesque eu, pretium quis, sem. Nulla consequat massa quis enim. Donec pede justo, fringilla vel, aliquet nec, vulputate eget, arcu. In enim justo, rhoncus ut, imperdiet a, venenatis vitae, justo. Nullam dictum felis eu pede mollis pretium. Integer tincidunt. Cras dapibus. Vivamus elementum semper nisi.Nullam dictum felis eu pede mollis pretium. Integer tincidunt. Cras dapibus. Vivamus elementum semper nisi.felis eu pede mollis pretium. Integer tincidunt. Cras dapibus.</p>

  <p class="body-text second">Quisque rutrum. Aenean imperdiet. Etiam ultricies nisi vel augue. Curabitur ullamcorper ultricies nisi. Nam eget dui. Etiam rhoncus. Maecenas tempus, tellus eget condimentum rhoncus, sem quam semper libero, sit amet adipiscing sem neque sed ipsum.felis pede mollis pretium. I am tincidunt. Cras dapibus.</p>

  <div class="signature" role="img" aria-label="Handwritten signature of the director"></div>
  <p class="sign-title">Director/Excecutive Director</p>

  <div class="web-band">
    <span>www.TQHarmClaimsDesk.example</span><span>|</span><span>www.PalmettoShieldCounsel.example</span>
  </div>
</section>

<section class="sheet envelope-back">
  <svg class="flap" width="444" height="66" viewBox="0 0 444 66" aria-hidden="true">
    <path d="M0 0 H444 L436 58 Q434 65 426 65 H18 Q10 65 8 58 Z" fill="var(--flap)"/>
  </svg>
  <span class="flap-mark"></span>
</section>

<section class="sheet envelope-front">
  <div class="brand">
    <span class="brand-dot"></span>
    <span class="brand-name">The Brambury Firm</span>
  </div>
  <p class="return-address">Post Office Box 4273<br>Lexington, SC 29458-4273</p>
  <div class="web-band">
    <span>www.TQHarmClaimsDesk.example</span><span>|</span><span>www.PalmettoShieldCounsel.example</span>
  </div>
</section>

</body>
</html>
```